New Tidewell 4 Group waste management business seeking web site

New project for business offering sustainable options within the waste industry.
Business called Tidewell 4 Group
Targeting the consumer & industry professionals the web site needs to be able to accommodate both.
Needs to have a modern clean feel.
Logo being designed by another pro and will be completed early next week and will be submitted soon after to be incorporated into the web page
Links to another web page i like very much to take into consideration.

Target Market(s)

Industry professionals, consumers and producers of all waste, Food, constructruction, commercial, retail .. etc..

Industry/Entity Type

Waste Management

Coding

Coded - Design and coding required

Number of Pages Required

5+ page

Font styles to use
Serif
Script

Requirements
Must have
• Flexabilty, all pages as in examples
Nice to have
• Open to offers you guys and gals are the pro's

```html
<!DOCTYPE html>
<html lang="en">
<head>
<meta charset="utf-8">
<title>Tidewell 4 Group</title>
<link rel="stylesheet" href="https://fonts.googleapis.com/css2?family=Source+Sans+3:wght@400;600;700&display=swap">
<style>
:root{
  --page:#e4e4e4;
  --white:#ffffff;
  --green:#4b8209;
  --green-dark:#3d6b06;
  --red:#aa0000;
  --red-deep:#8c1606;
  --red-band:#9a1d08;
  --ink:#222222;
  --grey:#f1f1f1;
  --form-bg:rgba(25,20,20,.78);
  --field:rgba(150,20,20,.55);
}
*{box-sizing:border-box;margin:0;padding:0}
html,body{width:1200px;height:2290px;overflow:hidden}
body{background:var(--page);font-family:"Source Sans 3",Arial,sans-serif;color:var(--ink);position:relative}
.site{position:absolute;left:15px;top:15px;width:1170px;height:2260px;background:var(--white);overflow:hidden}
.abs{position:absolute}

/* header */
.header{left:0;top:0;width:1170px;height:110px;background:var(--white);z-index:3}
.nav a{position:absolute;top:72px;font-size:16px;font-weight:600;color:var(--green);text-decoration:none;letter-spacing:.3px}
.brand{position:absolute;left:435px;top:66px;width:300px;text-align:center;font-size:26px;font-weight:700;color:var(--red);line-height:1}
.brand-dot{position:absolute;left:569px;top:26px;width:32px;height:32px;border-radius:50%;background:var(--red)}
.header-tab{position:absolute;left:420px;top:108px;z-index:4}

/* hero */
.hero{left:0;top:110px;width:1170px;height:490px;background:linear-gradient(180deg,#5f9ed9 0%,#a9cdea 32%,#8cc24c 55%,#4d8f1c 100%)}
.consult{left:806px;top:176px;width:310px;height:356px;background:var(--form-bg);border:1px solid rgba(255,255,255,.5);border-radius:4px}
.consult-title{left:794px;top:202px;width:340px;height:42px;background:var(--red);color:var(--white);font-weight:700;font-size:18px;text-align:center;line-height:42px;letter-spacing:.4px;box-shadow:0 2px 4px rgba(0,0,0,.4)}
.field{position:absolute;left:836px;width:282px;height:30px;background:var(--field);color:var(--white);font-size:13px;font-weight:600;padding:6px 12px}
.send{left:860px;top:482px;width:204px;height:31px;background:linear-gradient(#c40000,#8a0000);color:var(--white);font-size:14px;font-weight:700;text-align:center;line-height:31px;border-radius:2px}
.dots{left:557px;top:583px;display:flex;gap:8px}
.dots span{width:9px;height:9px;border-radius:50%;background:var(--white)}
.dots span:first-child{background:#222}

/* strategy band */
.band{left:0;top:600px;width:1170px;height:176px;background:linear-gradient(180deg,var(--red-band),#a8280c 60%,#8e1d08)}
.band h1{position:absolute;left:0;top:20px;width:1170px;text-align:center;color:var(--white);font-size:28px;font-weight:600;letter-spacing:.3px}
.band p{position:absolute;left:60px;top:60px;width:1050px;text-align:center;color:var(--white);font-size:14.5px;font-weight:600;line-height:20px}

/* services */
.service{position:absolute;top:725px;width:340px;text-align:center}
.service-icon{width:112px;height:112px;margin:0 auto;background:var(--green);border:3px solid var(--white);border-radius:6px;box-shadow:0 3px 6px rgba(0,0,0,.35);display:flex;align-items:center;justify-content:center}
.service-shadow{width:300px;height:10px;margin:4px auto 0;border-radius:50%;background:radial-gradient(ellipse,rgba(0,0,0,.22),rgba(0,0,0,0) 70%)}
.service h2{margin-top:12px;color:var(--green);font-size:21px;font-weight:700;letter-spacing:.4px}
.service p{margin:4px auto 0;width:310px;color:var(--green);font-size:13.5px;line-height:18px}
.btn{display:inline-block;background:var(--green);color:var(--white);font-weight:700;font-size:16px;border-radius:3px;text-decoration:none}
.service .btn{margin-top:18px;width:157px;height:38px;line-height:38px}

/* about + blog */
.about-band{left:0;top:1038px;width:1170px;height:385px;background:var(--red)}
.about-band h2{position:absolute;color:var(--white);font-size:27px;font-weight:700;letter-spacing:.3px}
.about-text{left:62px;top:1125px;width:545px;color:var(--white);font-size:13.5px;line-height:19px}
.about-text p+p{margin-top:19px}
.discover{left:62px;top:1295px;width:157px;height:40px;background:var(--white);color:var(--red);font-weight:700;font-size:16px;text-align:center;line-height:40px;border-radius:3px}
.post-img{position:absolute;left:670px;width:164px;height:123px;border:2px solid #e7e7e7;border-radius:3px}
.post-body{position:absolute;left:848px;width:280px;color:var(--white);font-size:13.5px;line-height:18px}
.post-body strong{display:block;font-weight:700;font-size:14px}

/* work */
.work-title{left:0;top:1453px;width:1170px;text-align:center;color:var(--green);font-size:27px;font-weight:700}
.work-card{position:absolute;top:1504px;width:350px}
.work-img{width:350px;height:236px}
.work-shadow{height:10px;margin:2px 14px 0;border-radius:50%;background:radial-gradient(ellipse,rgba(0,0,0,.2),rgba(0,0,0,0) 70%)}
.work-card h3{margin-top:18px;padding-left:3px;color:var(--green);font-size:20px;font-weight:700;letter-spacing:.3px}
.work-card p{margin-top:10px;padding-left:3px;font-size:13.5px;line-height:19px;color:var(--ink)}
.work-card .btn{margin-top:24px;margin-left:3px;width:157px;height:34px;line-height:34px;padding-left:12px;font-size:16px;position:relative}
.work-card .btn svg{position:absolute;right:12px;top:9px}

/* footer */
.footer{left:0;top:1942px;width:1170px;height:318px;background:linear-gradient(180deg,#e6e6e6,#f8f8f8 30%,#ffffff)}
.footer-shadow{left:40px;top:1942px;width:1090px;height:14px;border-radius:50%;background:radial-gradient(ellipse,rgba(0,0,0,.25),rgba(0,0,0,0) 70%)}
.f-col{position:absolute;top:2000px}
.f-col h4{font-size:16.5px;font-weight:700;color:#111;letter-spacing:.3px;margin-bottom:14px}
.f-col li{list-style:none;font-size:13.5px;font-weight:700;color:#222;line-height:21px;letter-spacing:.3px}
.contact-row{display:flex;gap:12px;font-size:13.5px;font-weight:700;color:#222;line-height:18px;margin-bottom:18px}
.contact-row svg{flex:none;margin-top:2px}
.social{display:flex;gap:8px;margin-left:30px}
.social span{width:22px;height:22px;border-radius:50%}
.footer-brand{left:880px;top:2085px;width:250px;text-align:center;font-size:24px;font-weight:700;color:var(--red)}
.footer-rule{left:62px;top:2223px;width:1050px;height:1px;background:#d8d8d8}
.copyright{left:0;top:2232px;width:1170px;text-align:center;font-size:11px;color:#444;letter-spacing:.3px}
</style>
</head>
<body>
<div class="site">

  <header class="abs header">
    <nav class="nav">
      <a style="left:85px">ABOUT</a>
      <a style="left:173px">SERVICES</a>
      <a style="left:277px">COLLABORATIONS</a>
      <a style="left:756px">WORK</a>
      <a style="left:838px">INSIGHT</a>
      <a style="left:932px">BLOG</a>
      <a style="left:1008px">CONTACT</a>
    </nav>
    <span class="brand-dot"></span>
    <div class="brand">Tidewell 4 Group</div>
  </header>
  <svg class="header-tab" width="330" height="28" viewBox="0 0 330 28" aria-hidden="true">
    <path d="M0 0 H330 C290 0 250 24 165 24 C80 24 40 0 0 0Z" fill="#ffffff"/>
  </svg>

  <div class="abs hero" role="img" aria-label="Photo of two hands cupped around a leafy tree on a green meadow under a blue sky"></div>

  <form class="abs consult"></form>
  <div class="abs consult-title">FREE CONSULTATION</div>
  <div class="field" style="top:263px">Name</div>
  <div class="field" style="top:302px">Email Address</div>
  <div class="field" style="top:343px">Phone Number</div>
  <div class="field" style="top:383px;height:90px">Message</div>
  <div class="abs send">SEND MESSAGE</div>
  <div class="abs dots"><span></span><span></span><span></span><span></span></div>

  <section class="abs band">
    <h1>TRULY SUSTAINABLE GROWTH STRATEGIES</h1>
    <p>Lorem ipsum dolor sit amet, consectetuer adipiscing elit, sed diam nonummy nibh euismod tincidunt ut laoreet dolore magna aliquam erat volutpat.<br>Ut wisi enim ad minim veniam, quis nostrud exerci tation ullamcorper suscipit lobortis nisl ut aliquip ex ea commodo consequat.</p>
  </section>

  <div class="service" style="left:36px">
    <div class="service-icon">
      <svg width="70" height="70" viewBox="0 0 70 70" fill="none" stroke="#fff" stroke-width="4">
        <circle cx="35" cy="35" r="29"/><circle cx="35" cy="35" r="19"/><circle cx="35" cy="35" r="9"/>
        <path d="M35 35 L60 10 M52 10 H60 V18"/>
      </svg>
    </div>
    <div class="service-shadow"></div>
    <h2>STRATEGIC CONSULTANCY</h2>
    <p>Lorem ipsum dolor sit amet, consectetuer adipis cing elit, sed diam nonummy nibh euismod tincidunt ut laoreet dolore magna aliquam erat.</p>
    <a class="btn">LEARN MORE</a>
  </div>
  <div class="service" style="left:415px">
    <div class="service-icon">
      <svg width="76" height="76" viewBox="0 0 76 76" fill="none" stroke="#fff" stroke-width="4" stroke-linecap="round">
        <path d="M12 8 V22 M28 8 V22 M6 22 H34 V34 A14 14 0 0 1 6 34Z M20 48 V58 Q20 68 32 68 H44 Q56 68 56 56 V50"/>
        <path d="M56 50 C44 44 44 22 58 8 C72 22 70 44 56 50Z M58 14 V44"/>
      </svg>
    </div>
    <div class="service-shadow"></div>
    <h2>SUSTAINABLE TECHNOLOGY</h2>
    <p>Lorem ipsum dolor sit amet, consectetuer adipis cing elit, sed diam nonummy nibh euismod tincidunt ut laoreet dolore magna aliquam erat.</p>
    <a class="btn">LEARN MORE</a>
  </div>
  <div class="service" style="left:795px">
    <div class="service-icon">
      <svg width="76" height="76" viewBox="0 0 76 76" fill="none" stroke="#fff" stroke-width="4" stroke-linecap="round">
        <circle cx="44" cy="42" r="24"/><path d="M38 8 H50 M44 8 V18 M44 42 L56 32 M4 32 H16 M8 42 H18 M4 52 H16"/>
      </svg>
    </div>
    <div class="service-shadow"></div>
    <h2>360 DELIVERY MANAGEMENT</h2>
    <p>Lorem ipsum dolor sit amet, consectetuer adipis cing elit, sed diam nonummy nibh euismod tincidunt ut laoreet dolore magna aliquam erat.</p>
    <a class="btn">LEARN MORE</a>
  </div>

  <section class="abs about-band">
    <h2 style="left:62px;top:30px">ABOUT US</h2>
    <h2 style="left:674px;top:30px">FROM THE BLOG</h2>
  </section>
  <div class="abs about-text">
    <p>Lorem ipsum dolor sit amet, consectetuer adipiscing elit, sed diam nonummy nibh euis mod tincidunt ut laoreet dolore magna aliquam erat volutpat. Ut wisi enim ad minim veniam, quis nostrud exerci tation ullamcorper suscipit lobortis nisl ut aliquip ex ea com modo consequat.</p>
    <p>Duis autem vel eum iriure dolor in hendrerit in vulputate velit esse molestie consequat, vel illum dolore eu feugiat nulla facilisis at vero eros et accumsan et iusto odio dignissim qui blandit praesent luptatum zzril delenit augue duis dolore te feugait nulla facilisi.</p>
  </div>
  <div class="abs discover">DISCOVER MORE</div>

  <div class="post-img" style="top:1115px;background:linear-gradient(135deg,#9fc6e4,#e9eef2 55%,#6b87a4)" role="img" aria-label="Photo of three colleagues in an office meeting"></div>
  <div class="post-body" style="top:1121px"><strong>Dec 12, 2015</strong><strong>Nam liber tempor cum soluta nobis</strong>Lorem ipsum dolor sit amet, consectetuer diam nonummy nibh euismod tincidunt ut aliquam erat volutpat.</div>
  <div class="post-img" style="top:1260px;background:linear-gradient(135deg,#1d4d63,#3a7e93 50%,#15384a)" role="img" aria-label="Aerial photo of a container ship at sea"></div>
  <div class="post-body" style="top:1266px"><strong>Dec 01, 2015</strong><strong>Nam liber tempor cum soluta nobis</strong>Lorem ipsum dolor sit amet, consectetuer diam nonummy nibh euismod tincidunt ut aliquam erat volutpat.</div>

  <h2 class="abs work-title">WORK</h2>
  <div class="work-card" style="left:40px">
    <div class="work-img" style="background:linear-gradient(180deg,#6aaee6 0%,#b9d6ef 25%,#8a9a3a 45%,#6e8a2a 65%,#3a5a6e 100%)" role="img" aria-label="Photo of tall marsh grass beside still water"></div>
    <div class="work-shadow"></div>
    <h3>LOREM IPSUM</h3>
    <p>Lorem ipsum dolor sit amet, consectetuer adipisci elit, sed diam nonummy nibh euismod tincidunt ut laoreet dolore magna aliquam erat volutpat.</p>
    <a class="btn">SEE MORE<svg width="20" height="16" viewBox="0 0 20 16" fill="none" stroke="#fff" stroke-width="3"><path d="M0 8 H17 M11 2 L17 8 L11 14"/></svg></a>
  </div>
  <div class="work-card" style="left:410px">
    <div class="work-img" style="background:linear-gradient(180deg,#3e8fd8 0%,#cfe3f5 30%,#24461e 48%,#2a5f93 62%,#1c3f6b 100%)" role="img" aria-label="Photo of a blue lake framed by forested hills and rocks"></div>
    <div class="work-shadow"></div>
    <h3>LOREM IPSUM</h3>
    <p>Lorem ipsum dolor sit amet, consectetuer adipisci elit, sed diam nonummy nibh euismod tincidunt ut laoreet dolore magna aliquam erat volutpat.</p>
    <a class="btn">SEE MORE<svg width="20" height="16" viewBox="0 0 20 16" fill="none" stroke="#fff" stroke-width="3"><path d="M0 8 H17 M11 2 L17 8 L11 14"/></svg></a>
  </div>
  <div class="work-card" style="left:780px">
    <div class="work-img" style="background:linear-gradient(180deg,#9db6cc 0%,#dfe6ea 28%,#7a8a3c 45%,#c8b04a 58%,#6f8090 78%,#4e5f6c 100%)" role="img" aria-label="Photo of a golden wetland with a bare tree reflected in water"></div>
    <div class="work-shadow"></div>
    <h3>LOREM IPSUM</h3>
    <p>Lorem ipsum dolor sit amet, consectetuer adipisci elit, sed diam nonummy nibh euismod tincidunt ut laoreet dolore magna aliquam erat volutpat.</p>
    <a class="btn">SEE MORE<svg width="20" height="16" viewBox="0 0 20 16" fill="none" stroke="#fff" stroke-width="3"><path d="M0 8 H17 M11 2 L17 8 L11 14"/></svg></a>
  </div>

  <footer class="abs footer"></footer>
  <div class="abs footer-shadow"></div>
  <div class="f-col" style="left:75px">
    <h4>QUICK LINKS</h4>
    <ul><li>ABOUT</li><li>COLLABORATIONS</li><li>WORK</li><li>INSIGHT</li><li>BLOG</li><li>CONTACT</li></ul>
  </div>
  <div class="f-col" style="left:301px">
    <h4>SERVICES</h4>
    <ul><li>STRATEGIC CONSULTANCY</li><li>SUSTAINABLE TECHNOLOGY</li><li>360 DELIVERY MANAGEMENT</li></ul>
  </div>
  <div class="f-col" style="left:603px">
    <h4>CONTACT INFO</h4>
    <div class="contact-row">
      <svg width="14" height="18" viewBox="0 0 14 18"><path d="M7 0 A7 7 0 0 1 14 7 C14 12 7 18 7 18 C7 18 0 12 0 7 A7 7 0 0 1 7 0Z" fill="#222"/><circle cx="7" cy="7" r="2.6" fill="#fff"/></svg>
      <div>Harbourline House<br>12 Fenwick Row<br>London | NW9 4QT</div>
    </div>
    <div class="contact-row">
      <svg width="18" height="14" viewBox="0 0 18 14"><path d="M1 4 Q9 -1 17 4 L15 6 L12 5 L12 3 Q9 2 6 3 L6 5 L3 6Z M4 7 H14 L16 14 H2Z" fill="#222"/></svg>
      <div>020 7946 0321</div>
    </div>
    <div class="contact-row">
      <svg width="18" height="13" viewBox="0 0 18 13"><rect width="18" height="13" rx="1" fill="#222"/><path d="M1 1 L9 8 L17 1" fill="none" stroke="#fff" stroke-width="1.5"/></svg>
      <div>hello@tidewell4group.co.uk</div>
    </div>
    <div class="social" aria-label="Social links">
      <span style="background:#3b5998"></span><span style="background:#2aa3ef"></span><span style="background:#d34836"></span>
    </div>
  </div>
  <div class="abs footer-brand">Tidewell 4 Group</div>
  <div class="abs footer-rule"></div>
  <div class="abs copyright">© 2015 TIDEWELL 4 GROUP LIMITED. ALL RIGHTS RESERVED.</div>

</div>
</body>
</html>
```